Redesign of the UI of a customer service platform

To improve the user experience of our customers, we need a new design for our agent interface of our customer service platform (lunorbit.com).
The focus will be on the dashboard and the inbox screens (see attached) along with the common UI elements (Buttons, menu, fonts, forms...)
We want a simple and distinctive design

Target Market(s)

Worldwide

Industry/Entity Type

It Service

Number of Pages Required

3 page

Font styles to use
Sans Serif

Requirements
Must have
• New Onboarding page: this is a new page that is shown to user the first time they login to the platform. This will replace the current onboarding screen (setup SMS, Setup widget...etc)
• Dashboard page: to access important information and activate services (see screenshot from current site)
• Inbox page: to manage all the interactions with customers. (see screenshot from current site)
• UI elements (buttons, menus, forms, tables, fonts, color palette)

```html
<!DOCTYPE html>
<html lang="en">
<head>
<meta charset="utf-8">
<title>lunorbit — Dashboard</title>
<link href="https://fonts.googleapis.com/css2?family=Mulish:wght@300;400;600;700&display=swap" rel="stylesheet">
<style>
:root{
  --topbar:#2b2b2b;
  --sidebar:#f25322;
  --sidebar-active:#c33a14;
  --sidebar-line:#d9431a;
  --page:#ffffff;
  --footer:#ececec;
  --text:#3a3a3a;
  --muted:#777;
  --grid:#8a8a8a;
  --orange-a:#ffa62b;--orange-b:#ff6a0f;--orange-bar:#ff8a25;
  --green-a:#a5e14a;--green-b:#5fcb28;--green-bar:#7fd23a;
  --blue-a:#11c2f8;--blue-b:#1a8ff0;--blue-bar:#19a6f0;
  --navy-a:#1f67a5;--navy-b:#0d2f57;--navy-bar:#123d6a;
  --plan:#17a6f5;
  --served:#4b97d4;
  --nonserved:#ff5a14;
  --panel-head:#f0f0f0;
  --border:#dcdcdc;
  --tick:#1a95ea;
}
*{box-sizing:border-box;margin:0;padding:0}
html,body{width:1200px;height:869px;overflow:hidden;font-family:"Mulish",sans-serif;color:var(--text);background:var(--page)}
.app{position:relative;width:1200px;height:869px}
.topbar{position:absolute;left:0;top:0;width:1200px;height:84px;background:var(--topbar);color:#fff}
.menu-toggle{position:absolute;left:55px;top:40px;width:28px}
.menu-toggle span{display:block;height:2px;background:#fff;margin-bottom:5px}
.brand{position:absolute;left:101px;top:30px;display:flex;align-items:center;gap:7px;font-size:20px;font-weight:700;color:#fff}
.brand-dot{width:14px;height:14px;border-radius:50%;background:#fff}
.top-icons{position:absolute;left:682px;top:34px;display:flex;gap:18px}
.top-icons svg{width:24px;height:24px}
.status{position:absolute;left:822px;top:38px;font-size:13px;display:flex;align-items:center;gap:6px}
.status .dot{width:10px;height:10px;border-radius:50%;background:#5fd13a}
.chev{width:10px;height:6px;margin-left:4px}
.user{position:absolute;left:944px;top:28px;display:flex;align-items:center;gap:8px;font-size:13px}
.avatar{width:30px;height:30px;border-radius:50%;background:linear-gradient(#d8c8b8,#8a7a6c)}
.sidebar{position:absolute;left:0;top:84px;width:245px;height:719px;background:var(--sidebar)}
.nav-item{display:flex;align-items:center;height:50px;padding-left:46px;font-size:18px;color:#fff;border-bottom:1px solid var(--sidebar-line)}
.nav-item.active{background:var(--sidebar-active)}
.nav-item svg{width:28px;height:24px;margin-right:16px}
.main{position:absolute;left:245px;top:84px;width:955px;height:719px}
.page-title{position:absolute;left:29px;top:27px;font-size:25px;font-weight:400;letter-spacing:.5px}
.range{position:absolute;left:740px;top:38px;font-size:11px;color:var(--muted);display:flex;align-items:center}
.stat{position:absolute;top:72px;width:209px;height:132px;color:#fff}
.stat .icon{position:absolute;left:20px;top:16px;width:46px;height:46px}
.stat .label{position:absolute;left:17px;top:79px;font-size:14.5px;line-height:19px}
.stat .value{position:absolute;right:13px;top:84px;font-size:27px;font-weight:300}
.stat .bar{position:absolute;left:0;top:140px;width:209px;height:4px}
.stat.clients{left:29px;background:linear-gradient(180deg,var(--orange-a),var(--orange-b))}
.stat.clients .bar{background:var(--orange-bar)}
.stat.tickets{left:247px;background:linear-gradient(180deg,var(--green-a),var(--green-b))}
.stat.tickets .bar{background:var(--green-bar)}
.stat.chat{left:465px;background:linear-gradient(180deg,var(--blue-a),var(--blue-b))}
.stat.chat .bar{background:var(--blue-bar)}
.stat.sms{left:683px;background:linear-gradient(180deg,var(--navy-a),var(--navy-b))}
.stat.sms .bar{background:var(--navy-bar)}
.panel{position:absolute;top:264px;width:429px;height:398px;border:1px solid var(--border);background:#fff}
.panel-head{height:39px;background:var(--panel-head);border-bottom:1px solid var(--border);padding:9px 20px;font-size:16.5px;color:#666}
.reports{left:29px}
.chart-title{position:absolute;left:25px;top:61px;font-size:15.5px}
.chart-sub{position:absolute;left:25px;top:87px;font-size:12.5px;color:var(--muted)}
.chart{position:absolute;left:15px;top:125px;width:387px;height:176px}
.chart text{font-family:"Mulish",sans-serif;font-size:8.5px;fill:#666}
.chart-filters{position:absolute;left:28px;top:308px;display:flex;gap:4px}
.chart-filters span{width:26px;height:26px;border-radius:50%}
.legend{position:absolute;right:24px;top:316px;display:flex;gap:22px;font-size:12px;color:#555}
.legend i{display:inline-block;width:11px;height:11px;margin-right:5px;vertical-align:-1px}
.plan{left:465px}
.plan-band{height:97px;background:var(--plan);color:#fff;position:relative}
.plan-name{position:absolute;left:23px;top:10px;font-size:17px}
.plan-name small{font-size:10px}
.plan-feats{position:absolute;left:24px;top:53px;display:flex;font-size:12.5px;line-height:16px}
.plan-feats div{display:flex;align-items:center;gap:8px}
.plan-feats svg{width:26px;height:24px}
.addon{position:relative;height:64px;border-bottom:1px solid var(--border);padding:21px 20px 0}
.addon:last-child{border-bottom:none}
.addon h3{font-size:15.5px;font-weight:400;line-height:18px}
.addon p{font-size:11px;color:#555;margin-top:3px}
.addon svg{position:absolute;right:26px;top:26px;width:22px;height:22px}
.footer{position:absolute;left:0;top:803px;width:1200px;height:66px;background:var(--footer);text-align:center;padding-top:24px;font-size:11.5px;color:#777}
</style>
</head>
<body>
<div class="app">
  <header class="topbar">
    <div class="menu-toggle"><span></span><span></span><span></span></div>
    <div class="brand"><span class="brand-dot"></span>lunorbit</div>
    <div class="top-icons">
      <svg viewBox="0 0 24 24"><ellipse cx="12" cy="11" rx="10" ry="7.5" fill="#777"/><path d="M5 16l-2 5 6-3z" fill="#777"/></svg>
      <svg viewBox="0 0 24 24"><rect x="4" y="7" width="16" height="10" rx="1" transform="rotate(-40 12 12)" fill="#777"/></svg>
      <svg viewBox="0 0 24 24"><circle cx="12" cy="12" r="11" fill="#777"/><text x="12" y="17" text-anchor="middle" font-size="15" font-weight="700" fill="#2b2b2b" font-family="Mulish,sans-serif">?</text></svg>
    </div>
    <div class="status"><span class="dot"></span>Available<svg class="chev" viewBox="0 0 10 6"><path d="M1 1l4 4 4-4" stroke="#888" fill="none"/></svg></div>
    <div class="user"><div class="avatar" role="img" aria-label="User profile photo"></div>Noel Varga<svg class="chev" viewBox="0 0 10 6"><path d="M1 1l4 4 4-4" stroke="#888" fill="none"/></svg></div>
  </header>

  <nav class="sidebar">
    <div class="nav-item active"><svg viewBox="0 0 28 24"><path d="M2 20a12 12 0 1 1 24 0z" fill="#fff"/><circle cx="14" cy="18" r="2.5" fill="#c33a14"/></svg>Dashboard</div>
    <div class="nav-item"><svg viewBox="0 0 28 24"><rect x="1" y="3" width="26" height="18" rx="2" fill="#fff" opacity=".85"/><path d="M1 5l13 9 13-9" stroke="#f25322" stroke-width="2" fill="none"/></svg>Inbox</div>
    <div class="nav-item"><svg viewBox="0 0 28 24"><rect x="5" y="7" width="18" height="10" rx="1" transform="rotate(-40 14 12)" fill="#fff" opacity=".85"/></svg>Tickets</div>
    <div class="nav-item"><svg viewBox="0 0 28 24"><circle cx="8" cy="7" r="4" fill="#fff" opacity=".85"/><circle cx="20" cy="7" r="4" fill="#fff" opacity=".85"/><circle cx="14" cy="10" r="4.5" fill="#fff"/><rect x="6" y="15" width="16" height="8" rx="4" fill="#fff"/></svg>Clients</div>
    <div class="nav-item"><svg viewBox="0 0 28 24"><path d="M13 2a10 10 0 1 0 10 11H13z" fill="#fff" opacity=".85"/><path d="M15 0v11h10A10 10 0 0 0 15 0z" fill="#fff"/></svg>Reports</div>
    <div class="nav-item"><svg viewBox="0 0 28 24"><circle cx="14" cy="12" r="8" fill="none" stroke="#fff" stroke-width="5" stroke-dasharray="4 2.3" opacity=".9"/><circle cx="14" cy="12" r="5" fill="#fff" opacity=".85"/></svg>Settings</div>
  </nav>

  <main class="main">
    <h1 class="page-title">Dashboard</h1>
    <div class="range">23 Dec 2016 - 07 Jan 2017<svg class="chev" viewBox="0 0 10 6"><path d="M1 1l4 4 4-4" stroke="#999" fill="none"/></svg></div>

    <section class="stat clients">
      <svg class="icon" viewBox="0 0 46 46" fill="#fff" opacity=".85"><circle cx="12" cy="12" r="6"/><circle cx="34" cy="12" r="6"/><circle cx="23" cy="17" r="7"/><rect x="11" y="26" width="24" height="16" rx="7"/></svg>
      <div class="label">Total Clients<br>Served/Non Served</div><div class="value">0/0</div><div class="bar"></div>
    </section>
    <section class="stat tickets">
      <svg class="icon" viewBox="0 0 46 46"><rect x="8" y="14" width="30" height="18" rx="2" transform="rotate(-45 23 23)" fill="#fff" opacity=".6"/></svg>
      <div class="label">Client Tickets<br>Closed/Opened</div><div class="value">0/0</div><div class="bar"></div>
    </section>
    <section class="stat chat">
      <svg class="icon" viewBox="0 0 46 46" fill="#fff" opacity=".85"><ellipse cx="24" cy="20" rx="20" ry="14"/><path d="M10 30l-4 10 12-7z"/></svg>
      <div class="label">Total Chat<br>Messages</div><div class="value">0/0</div><div class="bar"></div>
    </section>
    <section class="stat sms">
      <svg class="icon" viewBox="0 0 46 46" fill="none" stroke="#fff" stroke-width="3" opacity=".85"><ellipse cx="20" cy="18" rx="15" ry="11"/><path d="M30 30a14 10 0 0 0 8-12"/></svg>
      <div class="label">Total SMS<br>Messages</div><div class="value">0/0</div><div class="bar"></div>
    </section>

    <section class="panel reports">
      <div class="panel-head">Reports</div>
      <h2 class="chart-title" style="font-weight:400">Clients Total: Served vs non-served (Account)</h2>
      <p class="chart-sub">from 23 December 2016 to 07 January 2017</p>
      <svg class="chart" viewBox="0 0 440 200">
        <g stroke="var(--grid)" stroke-width="1">
          <line x1="24" y1="6" x2="438" y2="6"/><line x1="24" y1="40" x2="438" y2="40"/><line x1="24" y1="75" x2="438" y2="75"/>
          <line x1="24" y1="110" x2="438" y2="110"/><line x1="24" y1="145" x2="438" y2="145"/><line x1="24" y1="180" x2="438" y2="180"/>
        </g>
        <line x1="24" y1="6" x2="24" y2="180" stroke="var(--served)"/>
        <g text-anchor="end"><text x="16" y="9">100</text><text x="16" y="43">80</text><text x="16" y="78">60</text><text x="16" y="113">40</text><text x="16" y="148">20</text><text x="16" y="183">0</text></g>
        <g text-anchor="middle"><text x="46" y="192">10</text><text x="93" y="192">20</text><text x="139" y="192">30</text><text x="185" y="192">40</text><text x="232" y="192">50</text><text x="277" y="192">60</text><text x="324" y="192">70</text><text x="370" y="192">80</text><text x="416" y="192">90</text></g>
        <path d="M46 90 C69 90 70 101 93 101 C116 101 116 93 139 93 C162 93 162 71 185 71 C208 71 209 14 232 14 C255 14 254 65 277 65 C300 65 301 138 324 138 C347 138 347 123 370 123 C393 123 393 151 416 151" fill="none" stroke="var(--served)" stroke-width="1.6"/>
        <path d="M46 145 C69 145 70 110 93 110 C116 110 116 126 139 126 C162 126 162 110 185 110 C208 110 209 22 232 22 C255 22 254 91 277 91 C300 91 301 160 324 160 C347 160 347 127 370 127 C393 127 393 162 416 162" fill="none" stroke="var(--nonserved)" stroke-width="1.6"/>
        <g fill="var(--served)"><circle cx="46" cy="90" r="3"/><circle cx="93" cy="101" r="3"/><circle cx="139" cy="93" r="3"/><circle cx="185" cy="71" r="3"/><circle cx="232" cy="14" r="3"/><circle cx="277" cy="65" r="3"/><circle cx="324" cy="138" r="3"/><circle cx="370" cy="123" r="3"/><circle cx="416" cy="151" r="3"/></g>
        <g fill="var(--nonserved)"><circle cx="46" cy="145" r="3"/><circle cx="93" cy="110" r="3"/><circle cx="139" cy="126" r="3"/><circle cx="185" cy="110" r="3"/><circle cx="232" cy="22" r="3"/><circle cx="277" cy="91" r="3"/><circle cx="324" cy="160" r="3"/><circle cx="370" cy="127" r="3"/><circle cx="416" cy="162" r="3"/></g>
      </svg>
      <div class="chart-filters">
        <span style="background:var(--orange-b)"></span><span style="background:var(--green-b)"></span><span style="background:var(--blue-b)"></span><span style="background:var(--navy-b)"></span>
      </div>
      <div class="legend"><span><i style="background:var(--served)"></i>Served</span><span><i style="background:var(--nonserved)"></i>Non-Served</span></div>
    </section>

    <section class="panel plan">
      <div class="panel-head">Plan &amp; Add-ons</div>
      <div class="plan-band">
        <div class="plan-name">Plan <small>(Pro)</small></div>
        <div class="plan-feats">
          <div style="width:146px"><svg viewBox="0 0 26 24" fill="#fff"><circle cx="7" cy="7" r="3.5"/><circle cx="19" cy="7" r="3.5"/><circle cx="13" cy="9" r="4"/><rect x="5" y="14" width="16" height="9" rx="4"/></svg><span>Agents<br>Unlimited</span></div>
          <div style="width:152px"><svg viewBox="0 0 26 24" fill="#fff"><rect x="1" y="6" width="24" height="16" rx="2"/><rect x="9" y="2" width="8" height="5" fill="none" stroke="#fff" stroke-width="2"/><rect x="1" y="12" width="24" height="2" fill="#17a6f5"/></svg><span>Departments<br>Unlimited</span></div>
          <div><svg viewBox="0 0 26 24" fill="#fff"><path d="M5 2l5 1 1 5-3 2a12 12 0 0 0 6 6l2-3 5 1 1 5c-2 3-6 3-10 0S3 10 2 6z"/></svg><span>Phones<br>Unlimited</span></div>
        </div>
      </div>
      <div class="addon"><h3>Phones+SMS</h3><p>Proin nulla arcu nonummy luctus dictum eget fermentum et</p><svg viewBox="0 0 22 22"><circle cx="11" cy="11" r="11" fill="var(--tick)"/><path d="M6 11l3.5 3.5L16 8" stroke="#fff" stroke-width="2.4" fill="none"/></svg></div>
      <div class="addon"><h3>Paystrand</h3><p>Receive on time payments with Paystrand</p><svg viewBox="0 0 22 22"><circle cx="11" cy="11" r="11" fill="var(--tick)"/><path d="M6 11l3.5 3.5L16 8" stroke="#fff" stroke-width="2.4" fill="none"/></svg></div>
      <div class="addon"><h3>Pingwire</h3><p>Receive chat messages with Pingwire</p><svg viewBox="0 0 22 22"><circle cx="11" cy="11" r="11" fill="var(--tick)"/><path d="M6 11l3.5 3.5L16 8" stroke="#fff" stroke-width="2.4" fill="none"/></svg></div>
      <div class="addon"><h3>Chatnest Messengers</h3><p>Receive Chat messages with Chatnest Messenger</p><svg viewBox="0 0 22 22"><circle cx="11" cy="11" r="11" fill="var(--tick)"/><path d="M6 11l3.5 3.5L16 8" stroke="#fff" stroke-width="2.4" fill="none"/></svg></div>
    </section>
  </main>

  <footer class="footer">© 2017 Company Name&nbsp; All right reserved&nbsp; Term of Use</footer>
</div>
</body>
</html>
```